Cool wedding invitation

I need a creative graphic designer to create and design a hip, funky yet functional wedding invitation.

To give you an idea of what I am looking for I have create a Clipnest Board
http://www.clipnest-example.com/dalvorin/invitation/

Please provide your best 2 invitations.

Invitation #1 is designed to be printed on plastic. Use both sides
Invitation #2 is designed to be printed on cardboard

Don't be afraid to express your creativity.

Target Market(s)

This is a wedding invitation so the audience is primarily adults aged between 25 to 65.

Industry/Entity Type

Graphic Designer

Requirements
Nice to have
• The attached a colour palette outlines the colours the invitation may use.
• These colours will form the theme of the wedding.

```html
<!DOCTYPE html>
<html lang="en">
<head>
<meta charset="utf-8">
<title>Marlena &amp; Teo — Wedding Invitation</title>
<link rel="stylesheet" href="https://fonts.googleapis.com/css2?family=Francois+One&family=Open+Sans:wght@400&family=Yesteryear&display=swap">
<style>
  :root {
    --ink: #000000;
    --paper: #ffffff;
    --backdrop: #ffffff;
    --placeholder: #1a1a1a;
  }
  html, body {
    margin: 0;
    padding: 0;
    width: 1000px;
    height: 1200px;
    overflow: hidden;
    background: var(--backdrop);
  }
  .canvas {
    position: relative;
    width: 1000px;
    height: 1200px;
  }
  .invitation-card {
    position: absolute;
    left: 126px;
    top: 50px;
    width: 760px;
    height: 1080px;
    background: var(--paper);
  }
  .card-art {
    position: absolute;
    left: 0;
    top: 0;
    width: 1000px;
    height: 1200px;
  }
  .heading { font-family: "Francois One", sans-serif; fill: var(--ink); }
  .date-text { font-family: "Francois One", sans-serif; fill: var(--paper); }
  .location-note { font-family: "Open Sans", sans-serif; fill: var(--ink); }
  .sign-off { font-family: "Yesteryear", cursive; fill: var(--ink); }
  .ornament {
    position: absolute;
    background: var(--placeholder);
    border-radius: 6px;
  }
  .ornament--lovebirds { left: 443px; top: 185px; width: 114px; height: 48px; }
  .ornament--flourish-top { left: 467px; top: 234px; width: 66px; height: 18px; }
  .ornament--flourish-bottom { left: 435px; top: 1016px; width: 133px; height: 14px; }
</style>
</head>
<body>
<main class="canvas">
  <div class="invitation-card"></div>

  <svg class="card-art" viewBox="0 0 1000 1200" xmlns="http://www.w3.org/2000/svg">
    <g class="card-frame" fill="none" stroke="var(--ink)">
      <rect x="141" y="63" width="732" height="1052" stroke-width="4"/>
      <rect x="150" y="73" width="714" height="1032" stroke-width="2"/>
      <rect x="161" y="84" width="692" height="1010" stroke-width="1" stroke-dasharray="2 3"/>
    </g>

    <line class="rule" x1="257" y1="243" x2="745" y2="243" stroke="var(--ink)" stroke-width="2"/>

    <text class="heading couple-names" x="253" y="334" font-size="68" textLength="465" lengthAdjust="spacingAndGlyphs">MARLENA &amp; TEO</text>
    <text class="heading announcement" x="250" y="399" font-size="62" textLength="490" lengthAdjust="spacingAndGlyphs">ARE GETTING MARRIED</text>

    <g class="date-banner">
      <path d="M248 415 H742 L708 467 L742 520 H248 L285 467 Z" fill="var(--ink)"/>
      <polyline points="258,423 290,467 258,512" fill="none" stroke="var(--paper)" stroke-width="1" stroke-dasharray="2 2"/>
      <polyline points="732,423 702,467 732,512" fill="none" stroke="var(--paper)" stroke-width="1" stroke-dasharray="2 2"/>
      <text class="date-text" x="340" y="492" font-size="62" textLength="300" lengthAdjust="spacingAndGlyphs">12 • 07 • 2014</text>
    </g>

    <text class="heading invite-line" x="248" y="563" font-size="38" textLength="494" lengthAdjust="spacingAndGlyphs">YOU ARE INVITED TO WITNESS THEIR</text>
    <text class="heading love-word" x="248" y="805" font-size="318" textLength="497" lengthAdjust="spacingAndGlyphs">LOVE</text>

    <text class="heading venue-name" x="248" y="858" font-size="50" textLength="496" lengthAdjust="spacingAndGlyphs">LANTERN GALLERY</text>
    <text class="location-note" x="248" y="886" font-size="22" textLength="502" lengthAdjust="spacingAndGlyphs">PORTVALE - JUST UNDER THE OLD STONE BRIDGE</text>
    <text class="heading food-note" x="248" y="934" font-size="45" textLength="494" lengthAdjust="spacingAndGlyphs">WE HAVE GOOD FOOD AND MUSIC</text>

    <text class="sign-off" x="500" y="988" font-size="30" text-anchor="middle">Can't wait to see you there!</text>
  </svg>

  <div class="ornament ornament--lovebirds" role="img" aria-label="Two hummingbirds facing a small heart"></div>
  <div class="ornament ornament--flourish-top" role="img" aria-label="Decorative scroll flourish"></div>
  <div class="ornament ornament--flourish-bottom" role="img" aria-label="Decorative scroll flourish"></div>
</main>
</body>
</html>
```